Butcher shop

We have 2 butcher shops:

Shop 7, Ridgeway Court, Aberdeen NSW 2336
Ph 02 6519 4482

58 Partridge St, Scone NSW 2337
Ph 02 6538 2170

ABN 47 308 915 226

I would like this info on reverse of card and my personal info on front of card. I have a logo I would like to use also. Require a very smooth thick matte card, with colour both sides.

Front of card should say:

Lorna Tewsbury
Accounts

Ph 0427 615 903
E lornatewsbury@mailnest.example

Industry/Entity Type

Shop

Contact Information for Business Card

Lorna Tewsbury
Ph 0427 615 903

Logo Text

Tewsbury's Quality Meats

Logo styles of interest
Pictorial/Combination Logo
Requirements
Must have
• We use Century Gothic Font

```html
<!DOCTYPE html>
<html lang="en">
<head>
<meta charset="utf-8">
<title>Tewsbury's Quality Meats – Business Card</title>
<link rel="stylesheet" href="https://fonts.googleapis.com/css2?family=Urbanist:wght@400;500;700&display=swap">
<style>
  :root {
    --backdrop: #9a9a9a;
    --card: #ffffff;
    --sky: #8fd6f2;
    --ink: #231f20;
    --shadow: rgba(0, 0, 0, 0.35);
  }
  * { margin: 0; padding: 0; box-sizing: border-box; }
  html, body {
    width: 1200px;
    height: 1200px;
    overflow: hidden;
    background: var(--backdrop);
    font-family: "Urbanist", "Century Gothic", sans-serif;
    color: var(--ink);
  }
  .card {
    position: absolute;
    left: 164px;
    width: 869px;
    height: 488px;
    background: var(--card);
    box-shadow: 2px 3px 3px var(--shadow);
    overflow: hidden;
  }
  .card--front { top: 72px; }
  .card--back { top: 640px; }
  .card__band {
    position: absolute;
    left: 0;
    bottom: 0;
    width: 100%;
    height: 49px;
    background: var(--sky);
  }

  /* Front */
  .brand {
    position: absolute;
    left: 65px;
    top: 133px;
    width: 247px;
    height: 190px;
    display: flex;
    align-items: center;
    gap: 14px;
  }
  .brand__square {
    flex: 0 0 auto;
    width: 26px;
    height: 26px;
    background: var(--sky);
  }
  .brand__name {
    font-size: 30px;
    font-weight: 500;
    line-height: 1.15;
    color: var(--ink);
  }
  .person {
    position: absolute;
    left: 367px;
    top: 137px;
  }
  .person__name {
    font-size: 25px;
    font-weight: 700;
    letter-spacing: 1.5px;
    text-transform: uppercase;
  }
  .person__role {
    margin-top: 12px;
    font-size: 27px;
    font-weight: 400;
  }
  .contact {
    list-style: none;
    margin-top: 34px;
  }
  .contact__item {
    display: flex;
    align-items: baseline;
    font-size: 28px;
    font-weight: 400;
    line-height: 42px;
  }
  .contact__key {
    width: 29px;
    color: var(--sky);
    font-weight: 700;
    font-size: 26px;
  }

  /* Back */
  .locations {
    position: absolute;
    left: 0;
    top: 45px;
    width: 100%;
    text-align: center;
  }
  .location { margin-bottom: 46px; }
  .location__mark {
    display: block;
    width: 38px;
    height: 24px;
    margin: 0 auto 16px;
    background: var(--ink);
    border-radius: 3px;
  }
  .location__address,
  .location__phone {
    font-size: 27px;
    font-weight: 700;
    line-height: 33px;
  }
  .abn {
    position: absolute;
    left: 0;
    top: 384px;
    width: 100%;
    text-align: center;
    font-size: 23px;
    font-weight: 400;
  }
</style>
</head>
<body>
  <section class="card card--front">
    <div class="brand">
      <span class="brand__square" aria-hidden="true"></span>
      <span class="brand__name">Tewsbury's<br>Quality Meats</span>
    </div>
    <div class="person">
      <h1 class="person__name">Lorna Tewsbury</h1>
      <p class="person__role">Accounts</p>
      <ul class="contact">
        <li class="contact__item"><span class="contact__key">t</span>0427 615 903</li>
        <li class="contact__item"><span class="contact__key">e</span>lornatewsbury@mailnest.example</li>
      </ul>
    </div>
    <div class="card__band"></div>
  </section>

  <section class="card card--back">
    <div class="locations">
      <div class="location">
        <span class="location__mark" role="img" aria-label="Small brand emblem"></span>
        <p class="location__address">Shop 7, Ridgeway Court, Aberdeen NSW 2336</p>
        <p class="location__phone">Ph 02 6519 4482</p>
      </div>
      <div class="location">
        <span class="location__mark" role="img" aria-label="Small brand emblem"></span>
        <p class="location__address">58 Partridge St, Scone NSW 2337</p>
        <p class="location__phone">Ph 02 6538 2170</p>
      </div>
    </div>
    <p class="abn">ABN 47 308 915 226</p>
    <div class="card__band"></div>
  </section>
</body>
</html>
```